Kelekeleoliolimaiwaipeleke Fish Package

We need a package design for our Kelekeleoliolimaiwaipeleke Fish (not Bravlin fish). We plan to sell them at Hawaii stores to start and them take them to the mainland. We are looking for a package design that includes the front with a Kelekeleoliolimaiwaipeleke Fish (not a photo) and a back design with a photo of the fish (we will supply), information about the fish and nutrition information.

Target Market(s)

Premium market

Colors

Designer to choose colors to be used in the design.

Requirements
Must have
• See attached overview - also, it must include our logo (which we will provide)
Nice to have
• See attached overview

```html
<!DOCTYPE html>
<html lang="en">
<head>
<meta charset="utf-8">
<title>Nalu Reef – Kelekeleoliolimaiwaipeleke Fish Package</title>
<link href="https://fonts.googleapis.com/css2?family=Tinos:ital,wght@0,400;1,400&family=Open+Sans:wght@300;400;600;700&display=swap" rel="stylesheet">
<style>
  :root{
    --stage:#e8e9eb;
    --label-top:#3da3e6;
    --label-bottom:#5d60bf;
    --back-top:#3f7fce;
    --back-bottom:#6d8fd3;
    --ink:#1c2a5a;
    --white:#ffffff;
    --panel:#f7f8fb;
    --rule:#2a2a2a;
    --tick:#2b7fd0;
    --cross:#4a5a8a;
  }
  *{box-sizing:border-box;margin:0;padding:0}
  html,body{width:1200px;height:1200px;overflow:hidden;background:var(--stage)}
  .canvas{position:relative;width:1200px;height:1200px}

  /* Front label */
  .front-label{
    position:absolute;left:60px;top:140px;width:460px;height:900px;
    border-radius:10px;
    background:linear-gradient(180deg,var(--label-top) 0%,#4a86d8 45%,var(--label-bottom) 100%);
    color:var(--white);text-align:center;overflow:hidden;
  }
  .brand-name{
    font-family:"Open Sans",sans-serif;font-weight:300;
    letter-spacing:.12em;text-transform:uppercase;
  }
  .front-label .brand-name{font-size:52px;margin-top:34px;line-height:1}
  .front-label .product-name{
    font-family:"Tinos",serif;font-size:23px;margin-top:14px;color:var(--white);
  }
  .fish-illustration{
    display:block;margin:36px auto 0;width:220px;height:140px;border-radius:50% 40% 45% 50%;
    background:radial-gradient(ellipse at 45% 50%,#eef3fb 0%,#b9cbe8 60%,rgba(185,203,232,0) 75%);
  }
  .tagline{font-family:"Tinos",serif;font-size:17px;margin-top:38px;color:#e6ecfa}
  .serving-note{
    position:absolute;left:50%;top:700px;transform:translateX(-50%);
    width:360px;padding:10px 18px;border-radius:26px;background:var(--white);
    color:var(--ink);font-family:"Tinos",serif;font-size:15px;line-height:1.45;
  }
  .net-weight{
    position:absolute;right:18px;bottom:18px;width:42px;height:42px;border-radius:50%;
    background:var(--white);color:var(--ink);font-family:"Tinos",serif;font-size:14px;
    display:flex;align-items:center;justify-content:center;font-weight:700;
  }

  /* Back label */
  .back-label{
    position:absolute;left:570px;top:320px;width:580px;height:560px;border-radius:28px;
    background:linear-gradient(180deg,var(--back-top) 0%,var(--back-bottom) 100%);
    font-family:"Open Sans",sans-serif;color:var(--rule);
  }
  .nutrition-facts{
    position:absolute;left:20px;top:24px;width:140px;height:340px;background:var(--white);
    padding:6px 7px;font-size:7px;line-height:1.35;border:1px solid var(--rule);
  }
  .nutrition-facts h3{font-size:14px;font-weight:700;border-bottom:4px solid var(--rule);line-height:1.2}
  .nutrition-facts .row{display:flex;justify-content:space-between;border-bottom:.5px solid #888}
  .nutrition-facts .row.indent{padding-left:8px}
  .nutrition-facts .calories{display:flex;justify-content:space-between;font-size:12px;font-weight:700;border-bottom:3px solid var(--rule);padding:1px 0}
  .nutrition-facts .footnote{font-size:5.5px;margin-top:6px;line-height:1.3}

  .info-box{position:absolute;background:var(--panel);border-radius:6px;padding:8px 10px;font-size:8px;line-height:1.4}
  .info-box h4{display:inline-block;font-size:8px;font-weight:600;background:var(--white);border:1px solid #ccc;border-radius:3px;padding:0 5px;margin-bottom:4px}
  .ingredients{left:172px;top:24px;width:150px;height:150px;font-size:9.5px}
  .fish-story{left:334px;top:24px;width:226px;height:160px;font-size:6.5px}
  .fish-story h5{font-size:8px;font-weight:600;margin:2px 0 3px}
  .product-facts{left:172px;top:190px;width:388px;height:174px}

  .compare-table{border-collapse:collapse;font-size:6.5px;margin-top:2px}
  .compare-table th,.compare-table td{border:1px solid #555;padding:2px 4px;height:20px;text-align:center}
  .compare-table th{font-weight:400;height:16px}
  .compare-table td:first-child{text-align:left;width:56px}
  .compare-table td svg{display:block;margin:auto}
  .fish-photo{
    position:absolute;left:258px;top:32px;width:116px;height:96px;
    background:radial-gradient(ellipse at 50% 50%,#c9a97a 0%,#8a8f96 45%,#eef0f4 80%);
    border-radius:4px;
  }
  .fish-caption{position:absolute;left:250px;top:136px;width:132px;text-align:center;font-size:6.5px}

  .back-label .brand-name{
    position:absolute;left:0;right:0;top:392px;text-align:center;font-size:13px;color:#1e2f6a;
  }
</style>
</head>
<body>
<main class="canvas">

  <section class="front-label" aria-label="Front label">
    <h1 class="brand-name">Nalu Reef</h1>
    <h2 class="product-name">Kelekeleoliolimaiwaipeleke Fish</h2>
    <div class="fish-illustration" role="img" aria-label="Engraved-style drawing of a Kelekeleoliolimaiwaipeleke fish"></div>
    <p class="tagline">Premium kelekeleoliolimaiwaipeleke Fish a Hawaiian Treat</p>
    <p class="serving-note">If You Want The Best Flavors On Your Dish Just Add Some Citrus And Raspberry To Your Dish For More Perfection.</p>
    <span class="net-weight">5oz</span>
  </section>

  <section class="back-label" aria-label="Back label">
    <div class="nutrition-facts">
      <h3>Nutrition Facts</h3>
      <div class="row"><span>Serving size</span><b>1.4oz (40g)</b></div>
      <div class="row" style="border:none"><span>Amount per serving</span></div>
      <div class="calories"><span>Calories</span><span>140</span></div>
      <div class="row"><span></span><b>% Daily Value</b></div>
      <div class="row"><span><b>Total Fat</b> 0g</span><span>0%</span></div>
      <div class="row indent"><span>Saturated Fat 0g</span><span>0%</span></div>
      <div class="row indent"><span>Trans Fat 0g</span><span></span></div>
      <div class="row"><span><b>Cholesterol</b> 0mg</span><span>0%</span></div>
      <div class="row"><span><b>Sodium</b> 15mg</span><span>1%</span></div>
      <div class="row"><span><b>Total Carbohydrate</b> 36g</span><span>13%</span></div>
      <div class="row indent"><span>Dietary Fiber 0g</span><span>0%</span></div>
      <div class="row indent"><span>Total Sugars 26g</span><span></span></div>
      <div class="row indent"><span>Includes 26g Added Sugars</span><span>52%</span></div>
      <div class="row"><span><b>Protein</b> 0g</span><span></span></div>
      <div class="row"><span>Iron 0mg</span><span>0%</span></div>
      <p class="footnote">The % Daily Value tells you how much a nutrient in a serving contributes to a daily diet.</p>
    </div>

    <div class="info-box ingredients">
      <h4>Ingredients</h4>
      <p>Sugar, invert sugar syrup, corn starch, glucose syrup, acidity regulator (citric acid), aroma, glazing agent (carnauba wax, coconut oil), Colors: Turmeric, carmine.</p>
    </div>

    <div class="info-box fish-story">
      <h5>Kelekeleoliolimaiwaipeleke Fish:</h5>
      <p>This reef fish is found along the shallow lagoons of the islands. Its bright colors and bold markings make it a favorite sight for divers, and its name is sung in old chants passed between families for generations.</p>
      <h5>Reef Story</h5>
      <p>Our recipe honors that story with a soft, fruity chew made in small batches. Every piece is shaped by hand and packed fresh for island stores.</p>
    </div>

    <div class="info-box product-facts">
      <h4>Facts about this product</h4>
      <table class="compare-table">
        <tr><th></th><th>Kelekeleoliolimaiwaipeleke Fish</th><th>Bravlin Fish</th></tr>
        <tr><td>Free of Corn Syrup</td>
          <td><svg width="14" height="10"><path d="M1 5 L5 9 L13 1" stroke="var(--tick)" stroke-width="1.6" fill="none"/></svg></td>
          <td><svg width="10" height="10"><path d="M1 1 L9 9 M9 1 L1 9" stroke="var(--cross)" stroke-width="1.4"/></svg></td></tr>
        <tr><td>Natural Colors</td>
          <td><svg width="14" height="10"><path d="M1 5 L5 9 L13 1" stroke="var(--tick)" stroke-width="1.6" fill="none"/></svg></td>
          <td><svg width="10" height="10"><path d="M1 1 L9 9 M9 1 L1 9" stroke="var(--cross)" stroke-width="1.4"/></svg></td></tr>
        <tr><td>Non GMO</td>
          <td><svg width="14" height="10"><path d="M1 5 L5 9 L13 1" stroke="var(--tick)" stroke-width="1.6" fill="none"/></svg></td>
          <td><svg width="10" height="10"><path d="M1 1 L9 9 M9 1 L1 9" stroke="var(--cross)" stroke-width="1.4"/></svg></td></tr>
        <tr><td>Pineapple</td>
          <td><svg width="14" height="10"><path d="M1 5 L5 9 L13 1" stroke="var(--tick)" stroke-width="1.6" fill="none"/></svg></td>
          <td><svg width="10" height="10"><path d="M1 1 L9 9 M9 1 L1 9" stroke="var(--cross)" stroke-width="1.4"/></svg></td></tr>
      </table>
      <div class="fish-photo" role="img" aria-label="Photo of a Kelekeleoliolimaiwaipeleke fish"></div>
      <p class="fish-caption">Kelekeleoliolimaiwaipeleke Fish</p>
    </div>

    <p class="brand-name">Nalu Reef</p>
  </section>

</main>
</body>
</html>
```